Gelato Business Card

create a new business card using existing logo

Target Market(s)

B2B

Contact Information for Business Card

typical contact info: logo, address, email, phone, rep name

Colors
0355a3
33a6d7

Requirements
Must have
• a feel of high quality, luxury, happiness
• use cool, comforting color and texture of business card.
Nice to have
• "A Little Perfection Goes A Long Way!" TM
• or, "more quality, more flavor"
• or, "Flavor Matters"

```html
<!DOCTYPE html>
<html lang="en">
<head>
<meta charset="utf-8">
<title>Lucarelli's Business Card</title>
<link rel="stylesheet" href="https://fonts.googleapis.com/css2?family=Montserrat:wght@400;600;700&display=swap">
<style>
  :root {
    --backdrop: #e4e4e4;
    --card: #fbfbfb;
    --brand-blue: #3a3fa0;
    --accent-red: #c8202f;
    --text-grey: #444444;
    --web-orange: #f0a020;
  }
  html, body {
    margin: 0;
    padding: 0;
    overflow: hidden;
  }
  body {
    width: 1200px;
    height: 1200px;
    background: var(--backdrop);
    font-family: "Montserrat", sans-serif;
  }
  .card-sheet {
    display: block;
    width: 1200px;
    height: 1200px;
  }
  .card-face { fill: var(--card); }
  .frame-oval {
    fill: none;
    stroke: var(--brand-blue);
    stroke-width: 5;
  }
  .brand-name {
    font-family: "Montserrat", sans-serif;
    font-weight: 600;
    font-size: 46px;
    fill: var(--brand-blue);
  }
  .brand-dot { fill: var(--brand-blue); }
  .rep-name {
    font-weight: 700;
    font-size: 27px;
    fill: var(--brand-blue);
  }
  .rep-title {
    font-weight: 400;
    font-size: 18px;
    fill: var(--accent-red);
  }
  .contact-line {
    font-weight: 400;
    font-size: 18px;
    fill: var(--text-grey);
  }
  .web-highlight { fill: var(--web-orange); }
</style>
</head>
<body>
<svg class="card-sheet" viewBox="0 0 1200 1200" xmlns="http://www.w3.org/2000/svg">
  <!-- Front of card -->
  <g class="card-front" transform="translate(226 106)">
    <rect class="card-face" width="780" height="452"/>
    <ellipse class="frame-oval" cx="390" cy="226" rx="230" ry="92"/>
    <circle class="brand-dot" cx="262" cy="224" r="12"/>
    <text class="brand-name" x="410" y="241" text-anchor="middle">Lucarelli's</text>
  </g>

  <!-- Back of card -->
  <g class="card-back" transform="translate(226 638)">
    <rect class="card-face" width="780" height="450"/>
    <ellipse class="frame-oval" cx="390" cy="226" rx="340" ry="136"/>
    <g text-anchor="middle">
      <text class="rep-name" x="390" y="140">MARCO BELLINI</text>
      <text class="rep-title" x="390" y="166">Owner</text>
      <text class="contact-line" x="390" y="210">2240 Harbor View Rd., Suite 120</text>
      <text class="contact-line" x="390" y="233">Westbrook, MD 20716</text>
      <text class="contact-line" x="390" y="279">555-218-4470</text>
      <text class="contact-line" x="390" y="303">lucarellis@example.com</text>
      <text class="contact-line" x="390" y="330">www.<tspan class="web-highlight">lucarelligelato</tspan>.com</text>
    </g>
  </g>
</svg>
</body>
</html>
```